One Pager Fact Sheet Design

I need a couple of headers and footer designed to use for information security fact sheets to give to customers. Similar to the one listed below.

```html
<!DOCTYPE html>
<html lang="en">
<head>
<meta charset="utf-8">
<title>Fact Sheet Letterheads</title>
<link href="https://fonts.googleapis.com/css2?family=Oswald:wght@500;700&family=Roboto:wght@400;700&display=swap" rel="stylesheet">
<style>
  :root{
    --brand-red:#e3141b;
    --brand-grey:#595959;
    --paper:#ffffff;
    --canvas:#eeeeee;
    --ink-light:#ffffff;
    --photo-deep:#0d1f3a;
    --photo-mid:#2c5a8c;
    --photo-glow:#8fb6dc;
  }
  *{box-sizing:border-box;margin:0;padding:0}
  html,body{width:900px;height:1200px;overflow:hidden;background:var(--canvas)}
  body{position:relative;font-family:"Roboto",Arial,sans-serif}
  .sheet{position:absolute;top:330px;width:420px;height:540px;background:var(--paper);
    box-shadow:0 2px 6px rgba(0,0,0,.25)}
  .sheet--grey{left:20px;--band:var(--brand-grey)}
  .sheet--red{left:460px;--band:var(--brand-red)}
  .header,.footer{position:absolute;left:0;width:420px}
  .header{top:0;height:100px}
  .header svg,.footer svg{position:absolute;left:0;top:0}
  .band{fill:var(--band)}
  .brand{position:absolute;left:10px;top:7px;display:flex;align-items:center;gap:4px;
    color:var(--ink-light);font-family:"Oswald",sans-serif;font-weight:700;font-size:13px;letter-spacing:.2px}
  .brand__dot{width:12px;height:12px;border-radius:50%;background:var(--ink-light)}
  .topics{position:absolute;left:96px;top:5px;display:flex;gap:3px}
  .topic{width:26px;height:31px;border:1px solid rgba(255,255,255,.85);border-radius:3px;
    display:flex;flex-direction:column;align-items:center;padding-top:3px;color:var(--ink-light)}
  .topic svg{position:static;width:14px;height:14px}
  .topic span{font-size:3.6px;line-height:1.1;text-align:center;margin-top:2px}
  .title{position:absolute;left:10px;top:28px;color:var(--ink-light);font-family:"Oswald",sans-serif;line-height:1}
  .title__kicker{font-size:17px;font-weight:500}
  .title__main{font-size:20px;font-weight:700;margin-top:3px;letter-spacing:.2px}
  .footer{bottom:0;height:52px}
  .contact{position:absolute;color:var(--ink-light);font-size:10.5px;display:flex;align-items:center;gap:6px}
  .contact i{width:9px;height:9px;border-radius:50%;background:var(--ink-light);display:inline-block}
  .contact--web{left:12px;top:8px}
  .contact--mail{left:12px;top:29px}
  .social{position:absolute;color:var(--ink-light);font-size:6.4px;display:flex;align-items:center;gap:5px}
  .social i{width:8px;height:8px;border-radius:50%;background:var(--ink-light);display:inline-block}
</style>
</head>
<body>

<!-- Grey variant -->
<section class="sheet sheet--grey">
  <div class="header">
    <svg width="420" height="100" viewBox="0 0 420 100">
      <defs>
        <linearGradient id="cityA" x1="0" y1="0" x2="1" y2="1">
          <stop offset="0" stop-color="var(--photo-glow)"/>
          <stop offset=".45" stop-color="var(--photo-mid)"/>
          <stop offset="1" stop-color="var(--photo-deep)"/>
        </linearGradient>
      </defs>
      <rect x="280" y="0" width="140" height="86" fill="url(#cityA)" role="img" aria-label="Night city skyline with glowing network connection lines"/>
      <path class="band" d="M0 0 H300 Q318 62 420 84 V86 H0 Z"/>
    </svg>
    <div class="brand"><span class="brand__dot"></span>northvault</div>
    <div class="topics">
      <div class="topic"><svg viewBox="0 0 14 14" fill="none" stroke="#fff"><rect x="3" y="3" width="8" height="8"/></svg><span>IT security</span></div>
      <div class="topic"><svg viewBox="0 0 14 14" fill="none" stroke="#fff"><circle cx="7" cy="7" r="4.5"/></svg><span>Supply chain</span></div>
      <div class="topic"><svg viewBox="0 0 14 14" fill="none" stroke="#fff"><path d="M2 12 V5 L7 2 L12 5 V12 Z"/></svg><span>OT security</span></div>
      <div class="topic"><svg viewBox="0 0 14 14" fill="none" stroke="#fff"><circle cx="7" cy="5" r="2.5"/><path d="M2 13 Q7 6 12 13"/></svg><span>Insider threat</span></div>
      <div class="topic"><svg viewBox="0 0 14 14" fill="none" stroke="#fff"><path d="M7 1 L12 3 V7 Q12 11 7 13 Q2 11 2 7 V3 Z"/></svg><span>Physical security</span></div>
      <div class="topic"><svg viewBox="0 0 14 14" fill="none" stroke="#fff"><circle cx="7" cy="7" r="5"/><path d="M2 7 H12 M7 2 V12"/></svg><span>Interop comms</span></div>
    </div>
    <div class="title">
      <div class="title__kicker">FACT SHEET:</div>
      <div class="title__main">CrimsonLoop Malware SUMMARY</div>
    </div>
  </div>
  <div class="footer">
    <svg width="420" height="52" viewBox="0 0 420 52">
      <path fill="var(--brand-grey)" d="M140 11 H420 V50 H140 Z"/>
      <rect y="50" width="420" height="2" fill="var(--brand-red)"/>
      <path fill="var(--brand-red)" d="M0 0 H133 Q147 0 151 12 L160 40 Q164 52 178 52 H0 Z"/>
    </svg>
    <div class="contact contact--web"><i></i>www.northvault.net</div>
    <div class="contact contact--mail"><i></i>info@northvault.net</div>
    <div class="social" style="left:180px;top:16px"><i></i>network.example/loremipsum</div>
    <div class="social" style="left:180px;top:32px"><i></i>loremipsum.social.example</div>
    <div class="social" style="left:305px;top:16px"><i></i>http://loremipsum.com</div>
    <div class="social" style="left:305px;top:32px"><i></i>@loremipsum.com</div>
  </div>
</section>

<!-- Red variant -->
<section class="sheet sheet--red">
  <div class="header">
    <svg width="420" height="100" viewBox="0 0 420 100">
      <defs>
        <linearGradient id="cityB" x1="0" y1="0" x2="1" y2="1">
          <stop offset="0" stop-color="var(--photo-glow)"/>
          <stop offset=".45" stop-color="var(--photo-mid)"/>
          <stop offset="1" stop-color="var(--photo-deep)"/>
        </linearGradient>
      </defs>
      <rect x="280" y="0" width="140" height="86" fill="url(#cityB)" role="img" aria-label="Night city skyline with glowing network connection lines"/>
      <path class="band" d="M0 0 H300 Q322 70 292 82 H24 Q3 84 0 100 Z"/>
    </svg>
    <div class="brand"><span class="brand__dot"></span>northvault</div>
    <div class="topics">
      <div class="topic"><svg viewBox="0 0 14 14" fill="none" stroke="#fff"><rect x="3" y="3" width="8" height="8"/></svg><span>IT security</span></div>
      <div class="topic"><svg viewBox="0 0 14 14" fill="none" stroke="#fff"><circle cx="7" cy="7" r="4.5"/></svg><span>Supply chain</span></div>
      <div class="topic"><svg viewBox="0 0 14 14" fill="none" stroke="#fff"><path d="M2 12 V5 L7 2 L12 5 V12 Z"/></svg><span>OT security</span></div>
      <div class="topic"><svg viewBox="0 0 14 14" fill="none" stroke="#fff"><circle cx="7" cy="5" r="2.5"/><path d="M2 13 Q7 6 12 13"/></svg><span>Insider threat</span></div>
      <div class="topic"><svg viewBox="0 0 14 14" fill="none" stroke="#fff"><path d="M7 1 L12 3 V7 Q12 11 7 13 Q2 11 2 7 V3 Z"/></svg><span>Physical security</span></div>
      <div class="topic"><svg viewBox="0 0 14 14" fill="none" stroke="#fff"><circle cx="7" cy="7" r="5"/><path d="M2 7 H12 M7 2 V12"/></svg><span>Interop comms</span></div>
    </div>
    <div class="title">
      <div class="title__kicker">FACT SHEET:</div>
      <div class="title__main">CrimsonLoop Malware SUMMARY</div>
    </div>
  </div>
  <div class="footer">
    <svg width="420" height="52" viewBox="0 0 420 52">
      <path fill="var(--brand-grey)" d="M140 11 H420 V50 H140 Z"/>
      <rect y="50" width="420" height="2" fill="var(--brand-red)"/>
      <path fill="var(--brand-red)" d="M0 0 H133 Q147 0 151 12 L160 40 Q164 52 178 52 H0 Z"/>
    </svg>
    <div class="contact contact--web"><i></i>www.northvault.net</div>
    <div class="contact contact--mail"><i></i>info@northvault.net</div>
    <div class="social" style="left:180px;top:16px"><i></i>network.example/loremipsum</div>
    <div class="social" style="left:180px;top:32px"><i></i>loremipsum.social.example</div>
    <div class="social" style="left:305px;top:16px"><i></i>http://loremipsum.com</div>
    <div class="social" style="left:305px;top:32px"><i></i>@loremipsum.com</div>
  </div>
</section>

</body>
</html>
```